Marlow Optics PowerPoint Template

Marlow Optics needs a nice new corporate PowerPoint template, to be used for all types of presentations: sales, business development, finance, board/exec, etc.

I'd like to get a clean layout that reflects the brand (www.marlowoptics.example), has a bright, interesting title slide, and then minimal graphics on the content slides. Ideally the content slides would have a header, "mo" circle part of the Marlow Optics logo (either above or below), copyright/confidential footer, and page #.

About us: we have developed a revolutionary new array camera for mobile devices, providing depth at every pixel. Focus on any subject, change focus (even on multiple subjects) after you take the photo, capture linear measurements, scale and segment your images, change backgrounds, and apply filters, all from any device.
It's not just about megapixels anymore.
See www.marlowoptics.example for info.

Target Market(s)

The audience for 90% of our presentations is highly educated executives at technology companies.

Industry/Entity Type

Camera

Requirements
Nice to have
• It would be great to show an image in a phone UI on the title slide, similar to the approach on our website.
Helpful to have tagline on title slide: "A smart camera for your smartphone." It may also fit on the content slides - feel free to try.
I attached a product photo, but using it is completely optional.
I'd like the "mo" circle on the content slides, but the whole logo on the title slides.
Thanks!

```html
<!DOCTYPE html>
<html lang="en">
<head>
<meta charset="utf-8">
<title>About Marlow – Content Slide</title>
<link rel="stylesheet" href="https://fonts.googleapis.com/css2?family=Ubuntu:wght@300;400&family=Roboto+Condensed:wght@700&display=swap">
<style>
  :root {
    --navy: #0c3a52;
    --navy-text: #0d4a6c;
    --ink: #2f2f2f;
    --cell: #e9e7e8;
    --cell-text: #6d6d6d;
    --accent-blue: #2a8fc9;
    --footer: #575b5c;
    --white: #ffffff;
    --header-top: #ffffff;
    --header-bottom: #e8e8e8;
    --texture: #dcdcdc;
  }
  * { margin: 0; padding: 0; box-sizing: border-box; }
  html, body { width: 1200px; height: 900px; overflow: hidden; background: var(--white); }
  .slide {
    position: relative;
    width: 1200px;
    height: 900px;
    overflow: hidden;
    background: var(--white);
    font-family: "Ubuntu", sans-serif;
  }
  .backdrop-texture {
    position: absolute;
    left: 520px; top: 90px;
    width: 680px; height: 680px;
    background:
      radial-gradient(ellipse 62% 58% at 92% 48%, var(--texture) 0%, rgba(225,225,225,0.75) 35%, rgba(240,240,240,0.45) 62%, rgba(255,255,255,0) 100%);
  }
  .slide-header {
    position: absolute;
    left: 0; top: 0;
    width: 1200px; height: 100px;
    background: linear-gradient(to bottom, var(--header-top), var(--header-bottom));
  }
  .slide-title {
    position: absolute;
    left: 38px; top: 24px;
    font-size: 39px;
    font-weight: 400;
    color: var(--ink);
    letter-spacing: 0.2px;
  }
  .slide-title .brand { color: var(--navy-text); }
  .brand-mark {
    position: absolute;
    left: 1106px; top: 4px;
    width: 84px; height: 84px;
    border-radius: 50%;
    background: var(--navy);
    border: 4px solid var(--white);
    box-shadow: 0 0 0 1px #cfcfcf;
  }
  .section-heading {
    position: absolute;
    left: 72px; top: 168px;
    font-size: 36px;
    font-weight: 300;
    color: var(--ink);
  }
  .section-heading .highlight { color: var(--navy-text); font-weight: 400; }
  .data-table {
    position: absolute;
    left: 72px; top: 244px;
    width: 1034px; height: 284px;
    background: var(--white);
    padding: 5px 5px 6px 6px;
    box-shadow: 0 1px 5px rgba(0,0,0,0.18);
    display: grid;
    grid-template-columns: 338px 338px 339px;
    grid-template-rows: 66px 66px 65px 66px;
    gap: 3px 4px;
  }
  .data-table .cell {
    display: flex;
    align-items: center;
    padding-left: 18px;
    background: var(--cell);
    color: var(--cell-text);
    font-size: 21px;
    font-weight: 300;
  }
  .data-table .cell.head {
    background: var(--navy);
    color: var(--white);
    font-size: 25px;
    font-weight: 400;
  }
  .slide-footer {
    position: absolute;
    left: 0; top: 844px;
    width: 1200px; height: 56px;
    border-top: 8px solid var(--accent-blue);
    background: var(--footer);
    display: flex;
    justify-content: space-between;
    align-items: center;
    padding: 0 24px 0 30px;
    color: var(--white);
    font-family: "Roboto Condensed", sans-serif;
    font-weight: 700;
    font-size: 20px;
    letter-spacing: 0.4px;
  }
</style>
</head>
<body>
  <div class="slide">
    <div class="backdrop-texture" role="img" aria-label="Soft grey halftone dot texture fading into the background"></div>

    <header class="slide-header">
      <h1 class="slide-title">About <span class="brand">Marlow</span></h1>
      <div class="brand-mark" role="img" aria-label="Marlow Optics circle mark"></div>
    </header>

    <h2 class="section-heading">Table <span class="highlight">Content here</span></h2>

    <div class="data-table">
      <div class="cell head">Heading Content</div>
      <div class="cell head">Heading Content</div>
      <div class="cell head">Heading Content</div>
      <div class="cell">Sub Content Here</div>
      <div class="cell">Sub Content Here</div>
      <div class="cell">Sub Content Here</div>
      <div class="cell">Sub Content Here</div>
      <div class="cell">Sub Content Here</div>
      <div class="cell">Sub Content Here</div>
      <div class="cell">Sub Content Here</div>
      <div class="cell">Sub Content Here</div>
      <div class="cell">Sub Content Here</div>
    </div>

    <footer class="slide-footer">
      <span class="page-number">Page No. 00</span>
      <span class="copyright">Copyright@2013</span>
    </footer>
  </div>
</body>
</html>
```